Business Card Design Project

I am a property development company requiring a professional looking business card.
The name of the my company is PLW CANOPIES. I have attached a couple of designs that I have created on my own, that can give you an idea of what I am after.
Above the wording PLW CANOPIES, I have a orange arc above these words to signify the sun is begining to rise above the horizon.
I have a few designs; Middle Rays, Side Rays, Horizontals Rays which are OK, but I am looking for the better design.
The Rear design of the card is what I had came up with. If you have a better design, I am happy to see it.
The design of the card can follow what I have came up with, or it can be totally different. The fonts needs to be adjusted to another font that is more suitable.
The colours that I have used is what I think I would like to stick with. As I have mentioned, the orange arc is to signify the sun rising. If you have a better colour scheme, I would consider it.
Looking at dealing with first home buyers and proffesional people.
Business

```html
<!DOCTYPE html>
<html lang="en">
<head>
<meta charset="utf-8">
<title>PLW Canopies Business Card</title>
<link rel="stylesheet" href="https://fonts.googleapis.com/css2?family=Open+Sans:ital,wght@0,400;0,600;0,700;1,700&display=swap">
<style>
  :root {
    --backdrop: #e9e4df;
    --orange: #f26522;
    --orange-light: #f7892f;
    --orange-deep: #ee4f1c;
    --red: #e8232a;
    --white: #ffffff;
    --ink: #1a1a1a;
    --tagline: #ffe9a8;
  }
  * { margin: 0; padding: 0; box-sizing: border-box; }
  html, body {
    width: 1200px; height: 900px; overflow: hidden;
    background: var(--backdrop);
    font-family: "Open Sans", Arial, sans-serif;
  }
  .card-set {
    position: absolute; left: 60px; top: 290px;
    display: flex; gap: 40px;
  }
  .card {
    position: relative; width: 520px; height: 320px; overflow: hidden;
    box-shadow: 0 4px 14px rgba(0,0,0,0.18);
  }
  .sunburst {
    position: absolute; inset: 0;
    background: radial-gradient(ellipse at 50% 110%, var(--orange-light) 0%, var(--orange) 55%, var(--orange-deep) 100%);
  }
  /* Front */
  .card-front { display: flex; background: var(--white); }
  .contact-panel {
    position: relative; width: 238px; height: 100%; color: var(--white);
  }
  .contact-panel .sunburst {
    background: radial-gradient(ellipse at 0% 100%, var(--orange-light) 0%, var(--orange) 50%, var(--orange-deep) 100%);
  }
  .contact-details { position: relative; padding: 110px 0 0 28px; font-size: 13px; line-height: 1.35; }
  .person-name { font-weight: 700; font-size: 15px; }
  .person-role { margin-bottom: 20px; }
  .address { margin-bottom: 20px; }
  .contact-label { font-weight: 700; }
  .brand-panel {
    flex: 1; display: flex; flex-direction: column; align-items: center; justify-content: center;
    padding-top: 30px;
  }
  .brand-name { font-weight: 600; font-size: 27px; letter-spacing: 1px; color: var(--ink); line-height: 1; }
  .brand-sub { font-size: 11px; color: var(--ink); margin-top: 4px; }
  /* Back */
  .card-back { color: var(--white); }
  .back-brand {
    position: absolute; left: 0; right: 0; top: 98px; text-align: center;
  }
  .back-brand .brand-name { color: var(--white); font-size: 38px; font-weight: 400; letter-spacing: 1.5px; }
  .back-brand .brand-sub { color: var(--white); font-size: 14px; font-weight: 600; margin: 4px 0 0 150px; }
  .tagline {
    position: absolute; left: 0; right: 0; top: 188px; text-align: center;
    font-style: italic; font-weight: 700; font-size: 18px; color: var(--tagline);
  }
  .horizon-band { position: absolute; left: 0; bottom: 0; width: 520px; height: 72px; }
  .website {
    position: absolute; left: 0; right: 0; bottom: 14px; text-align: center;
    font-size: 13px; letter-spacing: 3px;
  }
</style>
</head>
<body>
  <main class="card-set">
    <section class="card card-front">
      <div class="contact-panel">
        <div class="sunburst" role="img" aria-label="Orange sunburst rays radiating from the lower left corner"></div>
        <div class="contact-details">
          <p class="person-name">Marcus Lee</p>
          <p class="person-role">Director</p>
          <p class="address">27 Harbour Lane Kirrawee<br>NSW 2232 Australia</p>
          <p><span class="contact-label">P</span> 0412 555 318</p>
          <p><span class="contact-label">E</span> marcus@plwcanopies.com.au</p>
          <p>www.plwcanopies.com.au</p>
        </div>
      </div>
      <div class="brand-panel">
        <p class="brand-name">PLW CANOPIES</p>
        <p class="brand-sub">Property Developments</p>
      </div>
    </section>

    <section class="card card-back">
      <div class="sunburst" role="img" aria-label="Orange sunburst rays rising from the horizon"></div>
      <div class="back-brand">
        <p class="brand-name">PLW CANOPIES</p>
        <p class="brand-sub">Property Developments</p>
      </div>
      <p class="tagline">Creating homes with Trust &amp; Openness</p>
      <svg class="horizon-band" viewBox="0 0 520 72" aria-hidden="true">
        <path d="M0 72 L0 48 Q260 -14 520 48 L520 72 Z" fill="var(--red)"/>
      </svg>
      <p class="website">www.plwcanopies.com.au</p>
    </section>
  </main>
</body>
</html>
```